Need Business Card for our Real Estate Business with Sales Executive's Picture

PANTONE 484 C ( RED)

PANTONE 2766 C ( BLUE

Industry/Entity Type

Real Estate

Contact Information for Business Card

Name, Mobile, email, & picture of Person
Agency Phone, address, Web address

Requirements
Must have
• Our Logo Colours, Agent Picture,

```html
<!DOCTYPE html>
<html lang="en">
<head>
<meta charset="utf-8">
<title>Dunewood Realty – Business Card</title>
<link href="https://fonts.googleapis.com/css2?family=Lato:wght@400;700&display=swap" rel="stylesheet">
<style>
  :root {
    --navy: #2b2d4f;
    --brand-red: #8e2a2f;
    --ink: #1f1f26;
    --paper: #ffffff;
    --backdrop: #e9e9ec;
    --photo-light: #f3f4f8;
    --photo-mid: #c9cfe0;
    --photo-deep: #34508f;
  }
  * { box-sizing: border-box; margin: 0; padding: 0; }
  html, body { width: 1200px; height: 900px; overflow: hidden; }
  body {
    background: var(--backdrop);
    font-family: "Lato", Arial, sans-serif;
    position: relative;
  }
  .card {
    position: absolute;
    width: 600px;
    height: 343px;
    box-shadow: 0 8px 22px rgba(0,0,0,0.18);
    overflow: hidden;
  }

  /* Back side */
  .card--back {
    left: 80px; top: 90px;
    background: var(--navy);
    color: var(--paper);
    display: flex;
    flex-direction: column;
    align-items: center;
    justify-content: center;
  }
  .brand {
    display: flex;
    align-items: center;
    gap: 12px;
    font-family: "Lato", Arial, sans-serif;
    font-weight: 400;
    text-transform: uppercase;
    letter-spacing: 0.14em;
    white-space: nowrap;
  }
  .brand__mark { width: 14px; height: 14px; background: currentColor; flex: none; }
  .card--back .brand { font-size: 40px; color: var(--paper); }
  .card--back .brand__mark { width: 18px; height: 18px; }
  .card--back .website {
    margin-top: 40px;
    font-size: 16px;
    letter-spacing: 0.03em;
  }

  /* Front side */
  .card--front {
    left: 520px; top: 467px;
    background: var(--paper);
  }
  .card--front .artwork { position: absolute; inset: 0; }
  .card--front .brand {
    position: absolute;
    left: 34px; top: 58px;
    font-size: 21px;
    letter-spacing: 0.08em;
    gap: 10px;
    color: var(--navy);
  }
  .card--front .brand__mark { width: 12px; height: 12px; }
  .agent {
    position: absolute;
    left: 36px; top: 112px;
  }
  .agent__name {
    color: var(--brand-red);
    font-weight: 700;
    font-size: 24px;
  }
  .agent__role {
    color: var(--ink);
    font-size: 15px;
    margin-top: 2px;
  }
  .contact {
    list-style: none;
    margin-top: 10px;
    font-size: 15px;
    color: var(--ink);
  }
  .contact li {
    display: flex;
    align-items: center;
    gap: 10px;
    height: 21px;
  }
  .contact svg { width: 13px; height: 13px; fill: var(--brand-red); flex: none; }
  .contact .no-icon { padding-left: 23px; }
  .band-web {
    position: absolute;
    right: 20px; bottom: 26px;
    color: var(--paper);
    font-size: 14px;
    letter-spacing: 0.02em;
    transform: rotate(-11deg);
    transform-origin: right bottom;
  }
</style>
</head>
<body>

  <section class="card card--back">
    <div class="brand"><span class="brand__mark"></span>Dunewood Realty</div>
    <p class="website">www.dunewoodrealty.com</p>
  </section>

  <section class="card card--front">
    <svg class="artwork" viewBox="0 0 600 343" width="600" height="343">
      <defs>
        <linearGradient id="agentTone" x1="0" y1="0" x2="0" y2="1">
          <stop offset="0" stop-color="#f3f4f8"/>
          <stop offset="0.45" stop-color="#c9cfe0"/>
          <stop offset="1" stop-color="#34508f"/>
        </linearGradient>
      </defs>
      <path d="M350 0 H600 V236 C520 258 430 282 350 300 Z" fill="url(#agentTone)" role="img" aria-label="Portrait photo of the sales executive in a blue suit"/>
      <path d="M60 343 C250 320 440 280 600 236 L600 252 C450 292 300 330 200 343 Z" fill="#8e2a2f"/>
      <path d="M200 343 C300 330 450 292 600 252 L600 343 Z" fill="#2b2d4f"/>
    </svg>

    <div class="brand"><span class="brand__mark"></span>Dunewood Realty</div>

    <div class="agent">
      <h1 class="agent__name">Daniel Hart</h1>
      <p class="agent__role">Manager</p>
      <ul class="contact">
        <li>
          <svg viewBox="0 0 24 24"><path d="M6.6 10.8a15.1 15.1 0 0 0 6.6 6.6l2.2-2.2a1 1 0 0 1 1-.25 11.4 11.4 0 0 0 3.6.57 1 1 0 0 1 1 1V20a1 1 0 0 1-1 1A17 17 0 0 1 3 4a1 1 0 0 1 1-1h3.5a1 1 0 0 1 1 1c0 1.25.2 2.45.57 3.57a1 1 0 0 1-.25 1z"/></svg>
          512 555 0140
        </li>
        <li>
          <svg viewBox="0 0 24 24"><path d="M7 1h10a2 2 0 0 1 2 2v18a2 2 0 0 1-2 2H7a2 2 0 0 1-2-2V3a2 2 0 0 1 2-2zm0 3v14h10V4zm5 15.5a1.2 1.2 0 1 0 0 2.4 1.2 1.2 0 0 0 0-2.4z"/></svg>
          512 555 0141
        </li>
        <li>
          <svg viewBox="0 0 24 24"><path d="M2 5h20v14H2zm2 2v.5l8 5 8-5V7zm0 3v7h16v-7l-8 5z"/></svg>
          info@dunewoodrealty.com
        </li>
        <li class="no-icon">48 Cedar Row, Houston, TX 77036</li>
      </ul>
    </div>

    <p class="band-web">www.dunewoodrealty.com</p>
  </section>

</body>
</html>
```